Attractive WP design (Astra) for our textile production and trading business

We need a design for our new website. We would like it to be based on the WP theme Astra.

1) Description of the business
Kelvaro GmbH is a textile company that is specialized in production and trading of high-quality cotton fabrics/products.

We…
• design and develop
• weave (incl. special weaving/embroidery technique)
• shear
• finish the products (Logo printing, packing)

Our products are…
• Swiss Ghutra
• Shemagh (=Yashmagh) (https://www.vontrema.ch/en/competence/clothing-textiles/clothing-for-arab-and-african-markets/#210)
• Desdasha’s (https://www.vontrema.ch/en/competence/clothing-textiles/clothing-for-arab-and-african-markets/#210)
• Emmas and Shawls
Emmas are traditional head coverings worn by Muslim man in Sudan. The cloth of exactly 5 yards in length is winded around the head like a turban. The cloth can be plain white, have a decorative trim or be colored. There are also matching scarfs.
• Brocade/Damask
• Atiku
• Teminor Voile (https://plovadesk.com/products/teminor-3?_pos=2&_sid=98a067e86&_ss=r)
--> Please see attached pictures of the different fabrics and products

2) Target audience and users
• (Foreign) wholesalers interested in trading with Kelvaro

3) Goals of the website
Kelvaro has been a family-run textile business for 17 years with no web presence. The majority of our historical sales have been based on pre-existing relationships or word-of-mouth connections. Now, we seek to diversify our customer base. For this, we want our first website/online presence in order to:

• Enable foreign wholesalers to discover Kelvaro as a supplier of Swiss quality fabric;
• Showcase both our current specific product line as well as our general manufacturing capabilities for new custom products;
• Enable inquiries/orders by interested parties

4) Design wishes
The design should reflect our high quality textiles. The design should be clean, inviting, friendly and professional. Colors can be chosen freely. Pictures should not overload sites but support our goal to attract and inspire future buyers.

If you have any questions, please reach out to us!

• the site will be multilingual (german/english/possibly french)

```html
<!DOCTYPE html>
<html lang="en">
<head>
<meta charset="utf-8">
<title>Kelvaro GmbH – Textiles</title>
<link rel="stylesheet" href="https://fonts.googleapis.com/css2?family=Tinos&family=Roboto:wght@400;500;700&family=Montserrat:wght@500&family=Nunito:wght@400&display=swap">
<style>
:root{
  --ink:#111;
  --text:#333;
  --muted:#555;
  --line:#222;
  --soft:#f6f6f6;
  --white:#fff;
  --field:#fdfafa;
  --field-border:#d6d0d0;
  --footer:#0a0a0a;
}
*{box-sizing:border-box;margin:0;padding:0}
html,body{width:1200px;height:3415px;overflow:hidden}
body{position:relative;background:var(--white);font-family:"Roboto",sans-serif;color:var(--text)}
.abs{position:absolute}

/* header */
.site-header{position:absolute;left:0;top:0;width:1200px;height:86px;background:var(--white)}
.brand{position:absolute;left:103px;top:14px;font-family:"Tinos",serif;font-size:40px;color:var(--ink);letter-spacing:1px}
.topbar{position:absolute;right:100px;top:10px;display:flex;align-items:center;gap:16px;font-size:15px;color:var(--ink);font-weight:500}
.topbar .item{display:flex;align-items:center;gap:6px}
.circle-icon{width:28px;height:28px;border:1px solid #999;border-radius:50%;display:flex;align-items:center;justify-content:center}
.lang{font-size:14px;color:#888;font-weight:400}
.lang b{color:var(--ink);font-weight:500;text-decoration:underline}
.main-nav{position:absolute;right:100px;top:53px;display:flex;gap:47px;font-size:14.5px;color:var(--ink)}
.main-nav span{position:relative;padding-bottom:6px}
.main-nav .active{border-bottom:2px solid var(--ink)}
.main-nav .active::after{content:"";position:absolute;left:50%;bottom:-2px;margin-left:-4px;border:4px solid transparent;border-bottom-color:var(--ink)}
.main-nav .search{display:flex;align-items:center;gap:6px}

/* hero */
.hero{position:absolute;left:0;top:86px;width:1200px;height:594px;background:linear-gradient(100deg,#bfb4a0 0%,#a79b83 30%,#6c6a50 55%,#8a7a62 75%,#cfc8bc 100%)}
.hero-title{position:absolute;left:100px;top:210px;font-family:"Tinos",serif;font-size:54px;color:var(--ink);letter-spacing:1px}
.hero-text{position:absolute;left:100px;top:272px;width:360px;font-size:16.5px;line-height:24px;color:var(--ink)}
.btn-dark{position:absolute;background:var(--ink);color:var(--white);font-weight:500;display:flex;align-items:center;justify-content:center}
.hero .btn-dark{left:100px;top:361px;width:152px;height:42px;font-size:14.5px}
.dots{position:absolute;left:561px;top:555px;display:flex;gap:10px}
.dots i{width:12px;height:12px;border:1.5px solid #fff;border-radius:50%}
.dots i.on{background:#fff}

/* sections */
.section-title{position:absolute;left:0;width:1200px;text-align:center;font-family:"Tinos",serif;font-size:38px;color:var(--ink)}
.section-title::after{content:"";position:absolute;left:569px;top:54px;width:62px;height:2px;background:var(--line)}
.welcome{position:absolute;left:0;top:680px;width:1200px;height:357px;background:var(--soft)}
.welcome p{position:absolute;left:150px;top:152px;width:900px;text-align:center;font-size:12.7px;line-height:24px;color:var(--text)}

.products{position:absolute;left:0;top:1037px;width:1200px;height:1028px;background:var(--white)}
.grid{position:absolute;left:100px;top:160px;display:grid;grid-template-columns:repeat(3,326px);grid-auto-rows:338px;gap:10px 11px}
.tile{position:relative;overflow:hidden}
.tile .label{position:absolute;left:0;bottom:0;width:100%;height:110px;display:flex;align-items:flex-end;justify-content:center;padding-bottom:14px;background:linear-gradient(rgba(0,0,0,0),rgba(0,0,0,.75));color:var(--white);font-weight:700;font-size:20px}
.t1{background:linear-gradient(160deg,#d8d8d8,#b4b4b4 60%,#2a2a2a 90%)}
.t2{background:linear-gradient(135deg,#f4f0ef,#d74a55 45%,#f1e9e9 70%,#c73040)}
.t3{background:linear-gradient(150deg,#eef2f5,#d9e2ea 60%,#8a7661 95%)}
.t4{background:linear-gradient(120deg,#3b2a22,#7d5a45 40%,#dcd3c8 60%,#c59a7d)}
.t5{background:linear-gradient(140deg,#c8342c,#e6b07a 35%,#e5e6ee 55%,#2d4fa8 80%,#b0282a)}
.t6{background:linear-gradient(160deg,#bdb8b0,#d7d3cc 50%,#8c8780 85%,#222)}
.btn-outline{position:absolute;left:501px;top:884px;width:198px;height:45px;border:1.5px solid #444;display:flex;align-items:center;justify-content:center;font-size:14.5px;font-weight:500;color:var(--ink)}

.services{position:absolute;left:0;top:2065px;width:1200px;height:444px;background:var(--soft)}
.cards{position:absolute;left:100px;top:132px;display:flex;gap:16px}
.card{width:238px;height:245px;background:var(--white);box-shadow:0 1px 4px rgba(0,0,0,.12);text-align:center;padding-top:30px}
.card svg{display:block;margin:0 auto}
.card h3{margin-top:10px;font-weight:400;font-size:19.5px;color:var(--ink)}
.card p{margin:10px auto 0;width:212px;font-size:12.5px;line-height:20px;color:var(--muted)}

.contact{position:absolute;left:0;top:2509px;width:1200px;height:574px;background:var(--white)}
.contact .lead{position:absolute;left:0;top:153px;width:1200px;text-align:center;font-family:"Nunito",sans-serif;font-size:17px;color:#444}
.field{position:absolute;background:var(--field);border:1px solid var(--field-border);border-radius:2px;font-size:13.5px;color:#555;padding:18px 0 0 22px}
.contact .btn-dark{left:524px;top:439px;width:152px;height:42px;font-size:14.5px}

.site-footer{position:absolute;left:0;top:3083px;width:1200px;height:332px;background:var(--footer);color:var(--white)}
.footer-brand{position:absolute;left:104px;top:70px;font-family:"Tinos",serif;font-size:62px}
.f-col{position:absolute;top:60px;font-size:13px}
.f-col h4{font-family:"Montserrat",sans-serif;font-weight:500;font-size:18.5px;margin-bottom:22px;position:relative}
.f-col h4::after{content:"";position:absolute;left:0;top:30px;width:31px;height:2px;background:var(--white)}
.f-col li{list-style:none;line-height:27px}
.f-contact div{display:flex;gap:6px;line-height:20px;margin-bottom:14px}
.news-input{border-bottom:1px solid #aaa;width:189px;padding-bottom:8px;font-size:13px}
.news-btn{margin-top:12px;width:103px;height:32px;background:var(--white);color:var(--ink);display:flex;align-items:center;justify-content:center;font-size:12.5px;font-weight:500}
.socials{display:flex;gap:9px;margin-top:18px}
.socials i{width:31px;height:31px;border-radius:50%;background:var(--white)}
.f-rule{position:absolute;left:100px;top:273px;width:1000px;height:1px;background:#333}
.copy{position:absolute;left:0;top:292px;width:1200px;text-align:center;font-size:13.5px}
</style>
</head>
<body>

<header class="site-header">
  <div class="brand">Kelvaro</div>
  <div class="topbar">
    <span class="item"><span class="circle-icon"><svg width="13" height="13" viewBox="0 0 24 24"><path d="M6.6 10.8a15 15 0 0 0 6.6 6.6l2.2-2.2a1 1 0 0 1 1-.25 11.4 11.4 0 0 0 3.6.57 1 1 0 0 1 1 1V20a1 1 0 0 1-1 1A17 17 0 0 1 3 4a1 1 0 0 1 1-1h3.5a1 1 0 0 1 1 1c0 1.25.2 2.45.57 3.6a1 1 0 0 1-.25 1z" fill="#111"/></svg></span>+41 71 555 20 18</span>
    <span class="item"><span class="circle-icon"><svg width="13" height="10" viewBox="0 0 26 20"><rect x="1" y="1" width="24" height="18" fill="#111"/><path d="M1 1l12 10L25 1" stroke="#fff" stroke-width="2" fill="none"/></svg></span>info@kelvaro-textil.ch</span>
    <span class="lang"><b>EN</b> | FR</span>
  </div>
  <nav class="main-nav">
    <span class="active">HOME</span><span>COMPANY</span><span>PRODUCTS</span><span>SERVICE</span><span>CONTACT US</span>
    <span class="search"><svg width="13" height="13" viewBox="0 0 20 20"><circle cx="8" cy="8" r="6" stroke="#111" stroke-width="2.5" fill="none"/><path d="M12.5 12.5L18 18" stroke="#111" stroke-width="2.5"/></svg>SEARCH</span>
  </nav>
</header>

<section class="hero" role="img" aria-label="Photo of a family in traditional white and brown robes walking along a palm-lined street">
  <h1 class="hero-title">KELVARO GMBH</h1>
  <p class="hero-text">Lorem ipsum dolor sit amet, consecttur adipiscing elit, sed do eiusmod tempor incididunt ut labore et dolore magna aliqua.</p>
  <div class="btn-dark">ORDER NOW</div>
  <svg class="abs" style="left:62px;top:284px" width="16" height="32" viewBox="0 0 16 32"><path d="M14 2L2 16l12 14" stroke="#fff" stroke-width="1.5" fill="none"/></svg>
  <svg class="abs" style="left:1122px;top:284px" width="16" height="32" viewBox="0 0 16 32"><path d="M2 2l12 14L2 30" stroke="#fff" stroke-width="1.5" fill="none"/></svg>
  <div class="dots"><i class="on"></i><i></i><i></i><i></i></div>
</section>

<section class="welcome">
  <h2 class="section-title" style="top:78px">WELCOME TO KELVARO</h2>
  <p>Lorem ipsum dolor sit amet, consectetur adipiscing elit, sed do eiusmod tempor incididunt ut labore et dolore magna aliqua. Quis ipsum suspendisse ultrices gravida. Risus commodo viverra maecenas accumsan lacus vel facilisis. Lorem ipsum dolor sit amet, consectetur adipiscing elit, sed do eiusmod tempor incididunt ut labore et dolore magna aliqua. Quis ipsum suspendisse ultrices gravida. Risus commodo viverra maecenas accumsan lacus vel facilisis. Lorem ipsum dolor sit amet, consectetur adipiscing elit, sed do eiusmod tempor incididunt ut labore et dolore magna aliqua. Quis ipsum suspendisse ultrices gravida. Risus commodo viverra maecenas accumsan lacus vel facilisis.</p>
</section>

<section class="products">
  <h2 class="section-title" style="top:83px">OUR PRODUCTS</h2>
  <div class="grid">
    <div class="tile t1" role="img" aria-label="Photo of folded fine white ghutra cotton"><span class="label">SWISS GHUTRA</span></div>
    <div class="tile t2" role="img" aria-label="Photo of red and white checked shemagh cloth"><span class="label">SHEMAGH</span></div>
    <div class="tile t3" role="img" aria-label="Photo of stacked white desdasha robes"><span class="label">DESDASHA’S</span></div>
    <div class="tile t4" role="img" aria-label="Photo of patterned embroidered shawls"><span class="label">EMMAS AND SHAWLS</span></div>
    <div class="tile t5" role="img" aria-label="Photo of red, blue and gold brocade fabrics"><span class="label">BROCADE/DAMASK</span></div>
    <div class="tile t6" role="img" aria-label="Photo of fine beige voile fabric"><span class="label">TEMINOR VOILE</span></div>
  </div>
  <div class="btn-outline">VIEW ALL PRODUCTS</div>
</section>

<section class="services">
  <h2 class="section-title" style="top:58px">WHAT WE DO</h2>
  <div class="cards">
    <div class="card">
      <svg width="56" height="56" viewBox="0 0 56 56" fill="none" stroke="#111" stroke-width="2"><rect x="5" y="5" width="46" height="46" stroke-dasharray="4 3"/><rect x="2" y="2" width="7" height="7" fill="#fff"/><rect x="47" y="2" width="7" height="7" fill="#fff"/><rect x="2" y="47" width="7" height="7" fill="#fff"/><rect x="47" y="47" width="7" height="7" fill="#fff"/><path d="M15 40L38 17l4 4-23 23h-4z"/><path d="M17 16l24 24"/></svg>
      <h3>Design and Develop</h3>
      <p>Lorem ipsuolor sit amet, consectetur adipiscing , sed do eiuspor incididunt ut labore et dolore magqua. Quis ipsum susptrices gravida.</p>
    </div>
    <div class="card">
      <svg width="56" height="56" viewBox="0 0 56 56" fill="none" stroke="#111" stroke-width="2"><path d="M17 6h18l-2 6H19zM19 44h14l2 6H17z"/><path d="M19 12l-1 32h16l-1-32"/><path d="M20 18l12 8M20 26l12 8M20 34l12 8"/><path d="M34 38c8 0 8 8 14 6"/></svg>
      <h3>Weave</h3>
      <p>Lorem ipsuolor sit amet, consectetur adipiscing , sed do eiuspor incididunt ut labore et dolore magqua. Quis ipsum susptrices gravida.</p>
    </div>
    <div class="card">
      <svg width="56" height="56" viewBox="0 0 56 56" fill="none" stroke="#111" stroke-width="2"><circle cx="14" cy="40" r="6"/><circle cx="26" cy="46" r="6"/><path d="M19 37L48 10M23 41L50 18"/><path d="M24 31l6 6"/></svg>
      <h3>Shear</h3>
      <p>Lorem ipsuolor sit amet, consectetur adipiscing , sed do eiuspor incididunt ut labore et dolore magqua. Quis ipsum susptrices gravida.</p>
    </div>
    <div class="card">
      <svg width="56" height="56" viewBox="0 0 56 56" fill="none" stroke="#111" stroke-width="2"><path d="M28 6l22 10v24L28 50 6 40V16z"/><path d="M6 16l22 10 22-10M28 26v24"/><path d="M17 11l22 10v8"/></svg>
      <h3>Finish the Products</h3>
      <p>Lorem ipsuolor sit amet, consectetur adipiscing , sed do eiuspor incididunt ut labore et dolore magqua. Quis ipsum susptrices gravida.</p>
    </div>
  </div>
</section>

<section class="contact">
  <h2 class="section-title" style="top:84px">CONTACT US</h2>
  <p class="lead">Get in touch set up a complimentary newwork assessment, Today</p>
  <div class="field" style="left:281px;top:196px;width:314px;height:53px">Name*</div>
  <div class="field" style="left:604px;top:196px;width:314px;height:53px">Phone*</div>
  <div class="field" style="left:281px;top:258px;width:314px;height:53px">Email*</div>
  <div class="field" style="left:604px;top:258px;width:314px;height:53px">Company*</div>
  <div class="field" style="left:281px;top:320px;width:637px;height:104px">Comments*</div>
  <div class="btn-dark">SUBMIT</div>
</section>

<footer class="site-footer">
  <div class="footer-brand">Kelvaro</div>
  <div class="f-col" style="left:403px">
    <h4>Quick Links</h4>
    <ul><li>Home</li><li>Services</li><li>Equipment Financing</li><li>Apply</li><li>Contact</li></ul>
  </div>
  <div class="f-col f-contact" style="left:619px">
    <h4>Contact Us</h4>
    <div><svg width="11" height="14" viewBox="0 0 12 16"><path d="M6 0a6 6 0 0 0-6 6c0 4.5 6 10 6 10s6-5.5 6-10a6 6 0 0 0-6-6z" fill="#fff"/><circle cx="6" cy="6" r="2.2" fill="#0a0a0a"/></svg><span>Lindenweg 14 &nbsp;CH – 9050<br>Aldenau Switzerland</span></div>
    <div><svg width="12" height="12" viewBox="0 0 24 24"><path d="M6.6 10.8a15 15 0 0 0 6.6 6.6l2.2-2.2a1 1 0 0 1 1-.25 11.4 11.4 0 0 0 3.6.57 1 1 0 0 1 1 1V20a1 1 0 0 1-1 1A17 17 0 0 1 3 4a1 1 0 0 1 1-1h3.5a1 1 0 0 1 1 1c0 1.25.2 2.45.57 3.6a1 1 0 0 1-.25 1z" fill="#fff"/></svg><span>Switzerland</span></div>
    <div><svg width="15" height="11" viewBox="0 0 26 20"><rect x="1" y="1" width="24" height="18" fill="#fff"/><path d="M1 1l12 10L25 1" stroke="#0a0a0a" stroke-width="2" fill="none"/></svg><span>info@kelvaro-textil.ch</span></div>
  </div>
  <div class="f-col" style="left:910px">
    <h4>Our Newsletter</h4>
    <div class="news-input">Enter Your Email...</div>
    <div class="news-btn">SUBMIT</div>
    <div class="socials"><i></i><i></i><i></i></div>
  </div>
  <div class="f-rule"></div>
  <p class="copy">Copyright © 2021 Kelvaro GmbH . All rights reserved.</p>
</footer>

</body>
</html>
```